Business Card Design for new logo

Business card Design for new logo. Follow colors from logo.
The company has offices in multiple comtries
Want to have some bulltes on the countries and also on the main services

Something like
USA*Dominican Republic*LATAM

Consulting*Healthcare IT*Tranformation

Industry/Entity Type

Information Technology

Contact Information for Business Card

Address, Phones, countries, name and position

Miron castell

Founder and CEO

947 Quarry Ln
Mill haven, PA 16835

Mcastell@novelquin.com

www.novelquin.com

717-352-6081

828-444-4444

```html
<!DOCTYPE html>
<html lang="en">
<head>
<meta charset="utf-8">
<title>Novelquin Health – Business Card</title>
<link href="https://fonts.googleapis.com/css2?family=Roboto:wght@400;500;700&display=swap" rel="stylesheet">
<style>
  :root {
    --brand-blue: #1f73b7;
    --brand-blue-deep: #1a63a0;
    --brand-orange: #f08a4b;
    --ink: #2b2b2b;
    --paper: #ffffff;
    --card-black: #0b0b0b;
    --backdrop: #2a2d31;
  }
  * { box-sizing: border-box; margin: 0; padding: 0; }
  html, body {
    width: 1200px; height: 900px; overflow: hidden;
    background: var(--backdrop);
    font-family: "Roboto", Arial, sans-serif;
  }
  .stage {
    width: 1200px; height: 900px;
    display: flex; align-items: center; justify-content: center; gap: 40px;
  }
  .card {
    width: 540px; height: 309px; border-radius: 22px;
    position: relative; overflow: hidden;
  }

  /* Front */
  .card-front { background: var(--paper); }
  .front-identity {
    position: absolute; top: 34px; left: 0; right: 0;
    display: flex; flex-direction: column; align-items: center;
  }
  .brand-line {
    display: flex; align-items: center; gap: 8px;
    color: var(--brand-blue); font-weight: 500; font-size: 17px; margin-bottom: 14px;
  }
  .brand-dot { width: 14px; height: 14px; border-radius: 50%; background: var(--brand-orange); }
  .person-name { color: var(--brand-blue); font-weight: 700; font-size: 30px; line-height: 1.1; }
  .person-title { color: var(--ink); font-size: 18px; margin-top: 2px; }

  .contact-band {
    position: absolute; top: 180px; left: 0; right: 0; height: 78px;
    background: var(--brand-blue);
    display: grid; grid-template-columns: 1.15fr 1fr 1.1fr;
    padding: 0 20px;
  }
  .contact-item { position: relative; padding-top: 22px; color: var(--paper); font-size: 13.5px; line-height: 1.35; }
  .contact-icon {
    position: absolute; top: -15px; left: 0;
    width: 30px; height: 30px; border-radius: 50%;
    background: var(--paper); border: 2px solid var(--brand-blue);
    display: flex; align-items: center; justify-content: center;
  }
  .contact-icon svg { width: 18px; height: 18px; }

  .country-strip {
    position: absolute; top: 258px; left: 0; right: 0; height: 30px;
    display: flex; align-items: center; justify-content: center; gap: 46px;
    color: var(--brand-blue); font-size: 14px; font-weight: 500;
  }
  .bullet::before {
    content: ""; display: inline-block; width: 7px; height: 7px; border-radius: 50%;
    background: var(--brand-orange); margin-right: 8px; vertical-align: middle;
  }
  .accent-edge {
    position: absolute; bottom: 0; left: 0; right: 0; height: 21px; background: var(--brand-orange);
  }

  /* Back */
  .card-back {
    background: var(--card-black);
    display: flex; flex-direction: column; align-items: center; justify-content: center;
  }
  .back-brand {
    display: flex; align-items: center; gap: 14px;
    color: var(--brand-blue); font-weight: 500; font-size: 46px; letter-spacing: 0.5px;
  }
  .back-brand .brand-dot { width: 26px; height: 26px; }
  .service-list {
    display: flex; gap: 26px; margin-top: 14px;
    color: #e9e9e9; font-size: 15px; list-style: none;
  }
</style>
</head>
<body>
<main class="stage">
  <section class="card card-front">
    <div class="front-identity">
      <div class="brand-line"><span class="brand-dot"></span>Novelquin Health</div>
      <h1 class="person-name">Miron Castell</h1>
      <p class="person-title">Founder and CEO</p>
    </div>

    <div class="contact-band">
      <div class="contact-item">
        <span class="contact-icon">
          <svg viewBox="0 0 24 24" fill="none" stroke="#f08a4b" stroke-width="2">
            <circle cx="12" cy="12" r="9"/><path d="M3 12h18M12 3c3 3 3 15 0 18M12 3c-3 3-3 15 0 18"/>
          </svg>
        </span>
        Mcastell@novelquin.com<br>www.novelquin.com
      </div>
      <div class="contact-item">
        <span class="contact-icon">
          <svg viewBox="0 0 24 24" fill="#f08a4b">
            <path d="M6.6 10.8a15 15 0 0 0 6.6 6.6l2.2-2.2a1 1 0 0 1 1-.25 11.4 11.4 0 0 0 3.6.57 1 1 0 0 1 1 1V20a1 1 0 0 1-1 1A17 17 0 0 1 3 4a1 1 0 0 1 1-1h3.5a1 1 0 0 1 1 1c0 1.25.2 2.45.57 3.6a1 1 0 0 1-.25 1z"/>
          </svg>
        </span>
        717-352-6081<br>828-444-4444
      </div>
      <div class="contact-item">
        <span class="contact-icon">
          <svg viewBox="0 0 24 24" fill="#f08a4b">
            <path d="M12 2a7 7 0 0 0-7 7c0 5.2 7 13 7 13s7-7.8 7-13a7 7 0 0 0-7-7zm0 9.5A2.5 2.5 0 1 1 12 6.5a2.5 2.5 0 0 1 0 5z"/>
          </svg>
        </span>
        947 Quarry Ln<br>Mill haven, PA 16835
      </div>
    </div>

    <div class="country-strip">
      <span class="bullet">USA</span>
      <span class="bullet">Dominican Republic</span>
      <span class="bullet">LATAM</span>
    </div>
    <div class="accent-edge"></div>
  </section>

  <section class="card card-back">
    <div class="back-brand"><span class="brand-dot"></span>Novelquin Health</div>
    <ul class="service-list">
      <li class="bullet">Consulting</li>
      <li class="bullet">Healthcare IT</li>
      <li class="bullet">Tranformation</li>
    </ul>
  </section>
</main>
</body>
</html>
```